Business Card Design Z9 MOTORS

Hi firstly I would like you to design a professional logo for my company. By using words " Z9 Auto Spares & Haulage".
We are an auto dismantling company where we buy wrecks/cars for dismantling and selling salvageable parts again.

Hi every one,

Thank you for posting the designs. But unfortunately non of these designs have the logo that I would prefer for my company. I will be branding the logo quite extensively, therefore please design some professional looking ones.

Thanks

Industry/Entity Type

Business

Contact Information for Business Card

Z9 Auto Spares & Haulage, 472 Kowhai Bend Rd, Fernmoor, Wellington
T: 04 7261048, F: 04 7261049, E: dean.morrow@z9motors.example.nz, W: www.z9motors.example.nz
Name: Dean L Morrow
Managing Director
Mob: 027418906

At the bottom of card " WE PAY TOP $$$$ FOR ANY UNWANTED VEHICLES FOR FOR DISMANTLING CALL US NOW 0800372815"

```html
<!DOCTYPE html>
<html lang="en">
<head>
<meta charset="utf-8">
<title>Z9 Auto Spares &amp; Haulage – Business Card</title>
<link href="https://fonts.googleapis.com/css2?family=Roboto+Condensed:ital,wght@0,400;0,700;1,700&display=swap" rel="stylesheet">
<style>
  :root {
    --backdrop: #1d4f63;
    --card-red: #e32d2d;
    --ink-white: #ffffff;
    --badge-black: #0d0d0d;
    --stripe-pink: #f6b9a8;
  }
  * { margin: 0; padding: 0; box-sizing: border-box; }
  html, body {
    width: 1200px;
    height: 1194px;
    overflow: hidden;
    background: var(--backdrop);
    font-family: "Roboto Condensed", "Arial Narrow", sans-serif;
  }
  .business-card {
    position: absolute;
    left: 60px;
    top: 305px;
    width: 1080px;
    height: 585px;
    background: var(--card-red);
    color: var(--ink-white);
    overflow: hidden;
  }
  .holder {
    position: absolute;
    right: 34px;
    top: 30px;
    text-align: right;
  }
  .holder-name { font-size: 44px; font-weight: 700; line-height: 1.1; }
  .holder-title { font-size: 29px; font-weight: 400; margin-top: 8px; }
  .holder-mobile { font-size: 29px; margin-top: 6px; display: flex; justify-content: flex-end; align-items: center; gap: 10px; }
  .badge {
    display: inline-flex;
    align-items: center;
    justify-content: center;
    width: 38px;
    height: 38px;
    border-radius: 50%;
    background: var(--badge-black);
    color: var(--ink-white);
    font-size: 22px;
    font-weight: 400;
    flex: none;
  }
  .brand-mark {
    position: absolute;
    left: 240px;
    width: 480px;
    top: 150px;
    display: flex;
    justify-content: center;
    align-items: center;
    gap: 18px;
  }
  .brand-dot { width: 60px; height: 60px; border-radius: 50%; background: var(--badge-black); flex: none; }
  .brand-name { font-size: 72px; font-weight: 700; line-height: 1; color: var(--ink-white); white-space: nowrap; }
  .stripes { position: absolute; top: 311px; width: 200px; height: 54px; }
  .stripes-left { left: 0; }
  .stripes-right { right: 0; }
  .company-name {
    position: absolute;
    left: 0; right: 0;
    top: 303px;
    text-align: center;
    font-size: 58px;
    font-weight: 700;
    line-height: 72px;
    white-space: nowrap;
  }
  .address {
    position: absolute;
    left: 0; right: 0;
    top: 382px;
    text-align: center;
    font-size: 26px;
  }
  .contact-row {
    position: absolute;
    left: 20px; right: 20px;
    top: 424px;
    display: flex;
    justify-content: center;
    align-items: center;
    font-size: 22px;
    white-space: nowrap;
  }
  .contact-row .item { display: flex; align-items: center; gap: 5px; margin: 0 7px; }
  .contact-row .badge { width: 32px; height: 32px; font-size: 19px; }
  .offer {
    position: absolute;
    left: 0; right: 0;
    top: 484px;
    text-align: center;
    font-size: 28px;
    text-transform: uppercase;
    white-space: nowrap;
  }
  .offer strong { font-weight: 700; font-style: italic; }
  .call-now {
    position: absolute;
    left: 0; right: 0;
    top: 528px;
    text-align: center;
    font-size: 29px;
    font-weight: 700;
    font-style: italic;
    text-transform: uppercase;
  }
</style>
</head>
<body>
  <div class="business-card">
    <div class="holder">
      <div class="holder-name">Dean L Morrow</div>
      <div class="holder-title">Managing Director</div>
      <div class="holder-mobile"><span class="badge">M</span><span>027418906</span></div>
    </div>

    <div class="brand-mark">
      <span class="brand-dot"></span>
      <span class="brand-name">Z9 MOTORS</span>
    </div>

    <svg class="stripes stripes-left" viewBox="0 0 200 54" preserveAspectRatio="none" aria-hidden="true">
      <g fill="var(--stripe-pink)">
        <rect x="0" y="0" width="200" height="4"/>
        <rect x="0" y="12" width="200" height="4"/>
        <rect x="0" y="24" width="200" height="4"/>
        <rect x="0" y="36" width="200" height="4"/>
        <rect x="0" y="48" width="200" height="4"/>
      </g>
    </svg>
    <svg class="stripes stripes-right" viewBox="0 0 200 54" preserveAspectRatio="none" aria-hidden="true">
      <g fill="var(--stripe-pink)">
        <rect x="0" y="0" width="200" height="4"/>
        <rect x="0" y="12" width="200" height="4"/>
        <rect x="0" y="24" width="200" height="4"/>
        <rect x="0" y="36" width="200" height="4"/>
        <rect x="0" y="48" width="200" height="4"/>
      </g>
    </svg>

    <h1 class="company-name">Z9 Auto Spares &amp; Haulage</h1>
    <p class="address">472 Kowhai Bend Rd, Fernmoor, Wellington</p>

    <div class="contact-row">
      <span class="item"><span class="badge">T</span>04 7261048,</span>
      <span class="item"><span class="badge">F</span>04 7261049,</span>
      <span class="item"><span class="badge">E</span>dean.morrow@z9motors.example.nz,</span>
      <span class="item"><span class="badge">W</span>www.z9motors.example.nz</span>
    </div>

    <p class="offer">We pay top <strong>$$$$</strong> for any unwanted vehicles for for dismantling</p>
    <p class="call-now">Call us now 0800372815</p>
  </div>
</body>
</html>
```